Ad Banner for Insight Net Panel

This banner is used in "Query Harbor" web site. This web site provides a single place for all employees to ask questions related to work. There will be dedicated subject matter experts to respond to all questions. The web site also provides "Talent Atlas" where employee can see the list of all experts in the company.
1. Banner size: 940x380
2. Business background: Provides maintenance, design and engineering, construction, machinery operation, material procurement and production management services for petrochemical and refinery business
3. We would like to see designs that
- Promote the ask questions in "Query Harbor" system
- Promote that company has experts in the areas of "Maintenance and Engineering" and can be found in "Talent Atlas"
- Encourage employees to advocate himself to be an expert by sending an email to a specific email address.
- Do not include picture of real people in the banner

```html
<!DOCTYPE html>
<html lang="en">
<head>
<meta charset="utf-8">
<title>Query Harbor – Insight Net Panel Banner</title>
<link rel="stylesheet" href="https://fonts.googleapis.com/css2?family=Share+Tech+Mono&display=swap">
<style>
  :root {
    --bg-core: #3b3535;
    --bg-edge: #1d3a43;
    --band: rgba(32, 78, 92, 0.55);
    --text: #e6ecee;
    --glow: #3fb4e6;
    --glow-soft: rgba(63, 180, 230, 0.35);
    --icon-light: #d9dcdd;
    --icon-shade: #8e9496;
  }
  * { margin: 0; padding: 0; box-sizing: border-box; }
  html, body { width: 1200px; height: 485px; overflow: hidden; background: #222; }
  .banner {
    position: relative;
    width: 1200px;
    height: 485px;
    overflow: hidden;
    font-family: "Share Tech Mono", monospace;
    color: var(--text);
    background:
      radial-gradient(ellipse 360px 300px at 600px 230px, rgba(40,120,160,0.45), transparent 70%),
      linear-gradient(180deg, var(--bg-edge) 0%, var(--bg-core) 22%, var(--bg-core) 78%, var(--bg-edge) 100%);
  }
  .band {
    position: absolute;
    background: var(--band);
  }
  .band--left { left: 0; top: 253px; width: 425px; height: 130px; }
  .band--right { right: 0; top: 255px; width: 370px; height: 118px; }

  .tools-icon {
    position: absolute;
    left: 120px; top: 95px;
    width: 120px; height: 120px;
    border-radius: 50%;
    background: radial-gradient(circle, rgba(210,215,217,0.55) 0%, rgba(140,148,150,0.25) 50%, transparent 72%);
  }
  .mail-icon {
    position: absolute;
    left: 958px; top: 122px;
    width: 126px; height: 100px;
  }

  .bulb-glow {
    position: absolute;
    left: 390px; top: 20px;
    width: 420px; height: 410px;
    background: radial-gradient(ellipse 150px 170px at 50% 42%, var(--glow-soft) 0%, rgba(63,180,230,0.15) 55%, transparent 80%);
  }
  .site-name {
    position: absolute;
    left: 450px; top: 140px;
    width: 300px;
    text-align: center;
    font-size: 44px;
    line-height: 1.15;
    color: #cfe9f4;
  }

  .experts-note {
    position: absolute;
    left: 32px; top: 262px;
    font-size: 22px;
    line-height: 28px;
  }
  .join-call {
    position: absolute;
    right: 20px; top: 265px;
    text-align: right;
  }
  .join-call__title { font-size: 25px; letter-spacing: 1px; margin-bottom: 8px; }
  .join-call__line { font-size: 21px; line-height: 27px; }

  .tagline {
    position: absolute;
    left: 0; right: 0; top: 440px;
    text-align: center;
    font-size: 21px;
    letter-spacing: 0.5px;
  }
</style>
</head>
<body>
  <div class="banner">
    <div class="band band--left"></div>
    <div class="band band--right"></div>

    <div class="tools-icon" role="img" aria-label="Crossed wrench and screwdriver icon"></div>

    <svg class="mail-icon" viewBox="0 0 126 100" aria-label="Envelope icon" role="img">
      <defs>
        <linearGradient id="envelope-face" x1="0" y1="0" x2="0" y2="1">
          <stop offset="0" stop-color="#f2f3f3"/>
          <stop offset="1" stop-color="#a9afb1"/>
        </linearGradient>
      </defs>
      <rect x="4" y="6" width="118" height="88" rx="8" fill="url(#envelope-face)"/>
      <path d="M8 14 L63 55 L118 14" fill="none" stroke="var(--icon-shade)" stroke-width="3"/>
      <path d="M8 88 L50 48 M118 88 L76 48" fill="none" stroke="#c4c8c9" stroke-width="2"/>
    </svg>

    <div class="bulb-glow" role="img" aria-label="Glowing neon light bulb outline with rays"></div>
    <div class="site-name">Query<br>Harbor</div>

    <p class="experts-note">
      Experts of<br>
      Maintenance and Engineering.<br>
      Seek out all our experts in<br>
      “Talent Atlas”.
    </p>

    <div class="join-call">
      <p class="join-call__title">BECOME AN EXPERT!</p>
      <p class="join-call__line">E-mail to us</p>
      <p class="join-call__line">mail@queryharbor.net</p>
    </div>

    <p class="tagline">Web site for all employees to ask questions related to work.</p>
  </div>
</body>
</html>
```